Bold Modern Creative Wine Label Needed for a Chardonnay

We need a modern, eye catching label, one that will appeal to millennials, but also attract the older more conservative crowd. We like the boldness of black on white but are open to your suggestions. Since the bottle type is a light green 'burgundy style' bottle, you should take that into account. The name of the brand is Ko`. The attached label is example of what we like very much. It is eye catching and bold and modern. Keep in mind that the bottle will be light green in color so black and white might not work so well. Use your creativity please! The label can be any size but needs to fit on this shape bottle. See attached photos. thanks!!

(Please no grapes or wine glasses or wine bottles featured on the label!)

Hi Designers, I just wanted to let you know that we received many great designs and we are sorting through them this week. The website is making it a bit difficult to create a 'poll' so this is taking longer than we expected. Thanks for all the great submissions!

```html
<!DOCTYPE html>
<html lang="en">
<head>
<meta charset="utf-8">
<title>Ko` Chardonnay Label</title>
<link rel="stylesheet" href="https://fonts.googleapis.com/css2?family=Barlow:wght@300;500&display=swap">
<style>
  :root {
    --label-tan: #e5aa6a;
    --label-tan-deep: #b98a55;
    --label-black: #0a0a0a;
    --label-width: 812px;
    --label-height: 1200px;
    --frame: 16px;
  }
  * { margin: 0; padding: 0; box-sizing: border-box; }
  html, body {
    width: var(--label-width);
    height: var(--label-height);
    overflow: hidden;
    background: var(--label-tan);
  }
  .wine-label {
    position: relative;
    width: var(--label-width);
    height: var(--label-height);
    background: var(--label-tan);
    font-family: "Barlow", "Helvetica Neue", Arial, sans-serif;
    font-weight: 300;
  }
  .label-panel {
    position: absolute;
    left: var(--frame);
    top: var(--frame);
    right: var(--frame);
    bottom: var(--frame);
    background: var(--label-black);
    overflow: hidden;
  }
  .brand-name {
    position: absolute;
    left: 0;
    top: 0;
    width: 600px;
    height: 320px;
  }
  .brand-name text {
    fill: var(--label-tan);
    font-family: "Barlow", "Helvetica Neue", Arial, sans-serif;
    font-weight: 500;
    font-size: 370px;
    letter-spacing: -30px;
  }
  .varietal {
    position: absolute;
    left: 36px;
    top: 391px;
    color: var(--label-tan);
    font-size: 58px;
    line-height: 1;
    letter-spacing: 0.165em;
    font-weight: 300;
    white-space: nowrap;
  }
  .pattern-band {
    position: absolute;
    left: 0;
    right: 0;
    top: 725px;
    bottom: 0;
    background: linear-gradient(160deg, var(--label-tan) 0%, var(--label-tan-deep) 100%);
    border-top: 3px solid var(--label-black);
  }
</style>
</head>
<body>
  <main class="wine-label">
    <section class="label-panel">
      <svg class="brand-name" viewBox="0 0 600 320" aria-label="Ko`">
        <text x="56" y="302">Ko`</text>
      </svg>
      <h1 class="varietal">CHARDONNAY</h1>
      <div class="pattern-band" role="img" aria-label="Geometric lattice pattern of squares crossed with diagonal lines in tan and black"></div>
    </section>
  </main>
</body>
</html>
```